Homepage für Unternehmensberatung
Zielgruppe
Wir sind eine Unternehmensberatung mit einem klaren Branchenfokus auf Banken / Finanzdienstleister.
Unsere Dienstleistungsprodukte lassen sich grob in folgende Themencluster unterteilen:
1)Strategieentwicklung
o IT-Strategie, IT-Architektur, IT-Bebauungsplan
2) Projektmanagement
o Projektportfoliomgmt., Programmmgmt., Projektmanagement, Projektcontrolling
3) Fachberatung
o Bankfachliche IT- Beratung mit Schwerpunkten Kredit, Wertpapiergeschäft,
Bankenaufsichtsrecht, Liquiditätsmanagement
o Anforderungsmanagement inkl. Aufbau von Bewertungs- und Priorisierungsmethoden
4) Prozessberatung/-optimierung
o Prozessanalyse, Prozessdesign, Prozessdokumentation
o Prozessoptimierung auf Basis etablierter Messmethoden
Unser Firmenname Lindenhofer hat für uns eine Doppelbedeutung:
1. Im Außenverhältnis: Wir verstehen uns als Lindenhofer unserer Kunden
2. Im Innenverhältnis: Wir pflegen einen partnerschaftlichen Umgang mit unseren
Mitarbeitern (Teamarbeit)
Aktuell sind wir ein kleines aber feines Team von erfahrenen und hochmotivierten Kollegen. Unsere Mitarbeiter sind ehemalige Führungskräfte sowie erfahrenen Unternehmensberater.
Aufgabenstellung
Entwurf / Design von 2 Seiten:
1. Seite / Startseite:
Simple und elegante Darstellung der oben genannten 4 Themencluster (z.B. Bild/Piktogramm, Textkasten) sowie einer Navigationsmöglichkeit zu folgenden Detailsichten:
• Unternehmen
• Beratungsangebot (siehe Themencluster)
• Partnerunternehmen
• Kontakt
2. Seite / 2. Ebene:
Entwurf einer Möglichkeit zur Erläuterung/Darstellung von Inhalten der Startseite.
Die Themencluster sollten auf jeder Ebene immer „anklickbar“/ zu sehen sein.
Logo
Das angehängte Logo ist in die Website einzubinden. Stil und Farben sollen übernommen werden bzw. sind Basis für das Design.
Lizenzen
Lizenz für eingesetzte Fotos und Illustrationen soll enthalten / Open-Source sein. Wenn nicht dann bitte zusätzliche Kosten angeben.

```html
<!DOCTYPE html>
<html lang="en">
<head>
<meta charset="utf-8">
<title>Lindenhofer – Management Consulting</title>
<link href="https://fonts.googleapis.com/css2?family=Roboto+Condensed:wght@700&family=Cinzel:wght@400&family=Open+Sans:wght@400;600&display=swap" rel="stylesheet">
<style>
  :root{
    --brand-blue:#1a78b3;
    --brand-blue-dark:#11608f;
    --tile-top:#3a98cf;
    --tile-bottom:#1769a0;
    --footer-bg:#2f2f2f;
    --footer-text:#9a9a9a;
    --tagline-bg:#5a5f63;
    --white:#ffffff;
    --logo-grey:#5b5b5b;
  }
  *{box-sizing:border-box;margin:0;padding:0}
  html,body{width:1200px;height:653px;overflow:hidden;background:#222}
  .page{position:relative;width:1200px;height:653px;overflow:hidden;font-family:"Open Sans",sans-serif}

  .site-header{position:absolute;left:0;top:0;width:1200px;height:52px;background:var(--brand-blue);border-bottom:2px solid var(--brand-blue-dark);z-index:3}
  .brand{position:absolute;left:180px;top:21px;width:284px;height:69px;background:var(--white);display:flex;align-items:center;gap:12px;padding-left:10px;z-index:4;box-shadow:0 1px 3px rgba(0,0,0,.3)}
  .brand-mark{width:46px;height:46px;border-radius:50%;background:var(--brand-blue);flex:none}
  .brand-name{font-family:"Open Sans",sans-serif;font-weight:600;font-size:25px;color:var(--logo-grey);letter-spacing:.3px}
  .main-nav{position:absolute;right:181px;top:27px;display:flex;gap:37px}
  .main-nav a{font-family:"Roboto Condensed",sans-serif;font-weight:700;font-size:16px;color:var(--white);text-decoration:none;text-transform:uppercase}

  .hero{position:absolute;left:0;top:52px;width:1200px;height:539px;
    background:linear-gradient(90deg,#3c3c3c 0%,#555 30%,#8c8f92 50%,#c9d7e4 68%,#9cc3e6 85%,#6e7378 100%)}

  .service-tile{position:absolute;width:172px;height:172px;display:flex;flex-direction:column;align-items:center;justify-content:center;text-align:center;z-index:2}
  .service-tile::before{content:"";position:absolute;left:25px;top:25px;width:122px;height:122px;transform:rotate(45deg);border-radius:10px;
    background:linear-gradient(135deg,var(--tile-top),var(--tile-bottom));border:3px solid #2a85bd;box-shadow:0 2px 6px rgba(0,0,0,.4);z-index:-1}
  .service-tile svg{width:34px;height:34px;margin-bottom:5px}
  .service-tile span{font-family:"Roboto Condensed",sans-serif;font-weight:700;font-size:15px;line-height:17px;color:var(--white);text-transform:uppercase}
  .tile-strategy{left:280px;top:109px}
  .tile-process{left:181px;top:204px}
  .tile-project{left:377px;top:207px}
  .tile-professional{left:278px;top:300px}

  .tagline{position:absolute;left:527px;top:509px;width:435px;height:36px;background:var(--tagline-bg);color:var(--white);
    font-family:"Cinzel",serif;font-size:24px;line-height:36px;text-align:center;letter-spacing:1px;z-index:2}

  .site-footer{position:absolute;left:0;top:591px;width:1200px;height:62px;background:var(--footer-bg);border-top:3px solid var(--brand-blue)}
  .copyright{position:absolute;left:179px;top:19px;font-size:11px;color:var(--footer-text)}
  .social-links{position:absolute;right:183px;top:15px;display:flex;gap:7px}
  .social-links a{display:block;width:22px;height:22px;border-radius:50%;background:#5e5e5e}
</style>
</head>
<body>
<div class="page">
  <header class="site-header">
    <nav class="main-nav">
      <a href="#">Company</a>
      <a href="#">Consulting Service</a>
      <a href="#">Partner Companies</a>
      <a href="#">Contact</a>
    </nav>
  </header>
  <a class="brand" href="#"><span class="brand-mark"></span><span class="brand-name">Lindenhofer</span></a>

  <section class="hero" role="img" aria-label="Smiling senior consultant in a light blue shirt in front of a grey night city skyline"></section>

  <div class="service-tile tile-strategy">
    <svg viewBox="0 0 34 34" fill="none" stroke="#fff" stroke-width="2.5"><circle cx="17" cy="17" r="14"/><path d="M23 11 15 15 11 23 19 19Z" fill="#fff" stroke="none"/></svg>
    <span>Strategy<br>Development</span>
  </div>
  <div class="service-tile tile-process">
    <svg viewBox="0 0 34 34" fill="none" stroke="#fff" stroke-width="3.5"><path d="M6 15A11 11 0 0 1 26 10"/><path d="M28 19A11 11 0 0 1 8 24"/><path d="M27 3v8h-8" stroke-width="3"/><path d="M7 31v-8h8" stroke-width="3"/></svg>
    <span>Process Consulting<br>and Optimization</span>
  </div>
  <div class="service-tile tile-project">
    <svg viewBox="0 0 34 34" fill="#fff"><rect x="12" y="4" width="10" height="7" rx="1"/><rect x="2" y="23" width="8" height="7" rx="1"/><rect x="13" y="23" width="8" height="7" rx="1"/><rect x="24" y="23" width="8" height="7" rx="1"/><path d="M16 11h2v5h11v7h-2v-5H18v5h-2v-5H7v5H5v-7h11z"/></svg>
    <span>Project Management</span>
  </div>
  <div class="service-tile tile-professional">
    <svg viewBox="0 0 34 34" fill="none" stroke="#fff" stroke-width="2.5"><path d="M17 3a10 10 0 0 0-6 18v3h12v-3a10 10 0 0 0-6-18z"/><path d="M12 28h10M14 32h6"/></svg>
    <span>Professional<br>Consulting Services</span>
  </div>

  <p class="tagline">Beautiful Tagline Goes Here</p>

  <footer class="site-footer">
    <p class="copyright">Copyright 2014. All rights reserved.</p>
    <nav class="social-links" aria-label="Social media">
      <a href="#" aria-label="Social network 1"></a>
      <a href="#" aria-label="Social network 2"></a>
      <a href="#" aria-label="Social network 3"></a>
      <a href="#" aria-label="Social network 4"></a>
      <a href="#" aria-label="Social network 5"></a>
    </nav>
  </footer>
</div>
</body>
</html>
```